A Gulf Book about Mother - Need Cover Design

An Arabic book tells about the mother, a love letter
Introducing the reader to what the mother is doing for the sake of the family - the tenderness of the baby and a lot of advice to love and respect the mother
The title of the book : الواحة - نغمة صباح
Meaning in English (oasis - morning tune)
The size of the book is small so colors must be bright and expressive
Add to the title of the book
Year - 2018 - 1440
Publishing logo

Target Market(s)
families - student
Requirements
Must have
- Design must be away from any images of people directly
Nice to have
- the book is 150 page that i want The be bright colors give meaning to the message of love from the children to the mother --- for example (hearts - leaves - flowers ... etc)

```html
<!DOCTYPE html>
<html lang="ar" dir="rtl">
<head>
<meta charset="utf-8">
<title>الواحة - نغمة صباح</title>
<link href="https://fonts.googleapis.com/css2?family=Noto+Sans+Arabic:wght@400;700&display=swap" rel="stylesheet">
<style>
  :root {
    --paper: #ffffff;
    --crop: #9a9a9a;
    --cover-top: #c90b5b;
    --cover-mid: #8e1445;
    --cover-bottom: #521330;
    --spine-top: #5e1133;
    --spine-bottom: #431024;
    --ink: #ffffff;
  }
  html, body {
    margin: 0;
    padding: 0;
    width: 1200px;
    height: 604px;
    overflow: hidden;
    background: var(--paper);
  }
  .sheet {
    position: relative;
    width: 1200px;
    height: 604px;
    font-family: "Noto Sans Arabic", sans-serif;
    color: var(--ink);
  }
  .crop-marks {
    position: absolute;
    inset: 0;
  }
  .cover {
    position: absolute;
    top: 24px;
    height: 556px;
    background: linear-gradient(180deg, var(--cover-top) 0%, var(--cover-mid) 55%, var(--cover-bottom) 100%);
  }
  .cover--front { left: 24px; width: 549px; }
  .cover--back { left: 625px; width: 549px; }
  .spine {
    position: absolute;
    top: 24px;
    left: 573px;
    width: 52px;
    height: 556px;
    background: linear-gradient(180deg, var(--spine-top), var(--spine-bottom));
  }
  .heart-icon {
    position: absolute;
    left: 253px;
    top: 132px;
    width: 48px;
    height: 48px;
  }
  .book-title {
    position: absolute;
    left: 0;
    width: 549px;
    top: 250px;
    margin: 0;
    text-align: center;
    font-weight: 400;
    font-size: 54px;
    line-height: 1.2;
  }
  .year {
    position: absolute;
    left: 60px;
    top: 522px;
    margin: 0;
    font-size: 13px;
    font-weight: 700;
    direction: ltr;
  }
  .publisher {
    position: absolute;
    display: flex;
    flex-direction: column;
    align-items: center;
    gap: 6px;
    font-weight: 700;
    white-space: nowrap;
  }
  .publisher__mark {
    width: 30px;
    height: 30px;
    border: 2px solid var(--ink);
    box-sizing: border-box;
  }
  .publisher--front { left: 409px; top: 464px; width: 90px; font-size: 13px; }
  .publisher--back { left: 251px; top: 464px; width: 90px; font-size: 13px; }
  .publisher--spine { left: 0; top: 512px; width: 52px; font-size: 8px; gap: 4px; }
  .publisher--spine .publisher__mark { width: 16px; height: 16px; border-width: 1.5px; }
  .spine-title {
    position: absolute;
    left: 8px;
    top: 70px;
    margin: 0;
    width: 36px;
    writing-mode: vertical-rl;
    font-size: 28px;
    font-weight: 400;
    line-height: 36px;
    white-space: nowrap;
  }
</style>
</head>
<body>
<div class="sheet">
  <svg class="crop-marks" width="1200" height="604" viewBox="0 0 1200 604" aria-hidden="true">
    <g stroke="var(--crop)" stroke-width="0.8">
      <line x1="0" y1="24" x2="16" y2="24"/><line x1="24" y1="0" x2="24" y2="16"/>
      <line x1="1184" y1="24" x2="1200" y2="24"/><line x1="1174" y1="0" x2="1174" y2="16"/>
      <line x1="0" y1="580" x2="16" y2="580"/><line x1="24" y1="588" x2="24" y2="604"/>
      <line x1="1184" y1="580" x2="1200" y2="580"/><line x1="1174" y1="588" x2="1174" y2="604"/>
      <line x1="573" y1="0" x2="573" y2="16"/><line x1="625" y1="0" x2="625" y2="16"/>
      <line x1="573" y1="588" x2="573" y2="604"/><line x1="625" y1="588" x2="625" y2="604"/>
    </g>
  </svg>

  <section class="cover cover--back" role="img" aria-label="Soft pattern of leaves and branches over a magenta gradient">
    <div class="publisher publisher--back">
      <span class="publisher__mark"></span>
      <span class="publisher__name">دار النخيل</span>
    </div>
  </section>

  <section class="spine">
    <h2 class="spine-title">الواحة - نغمة صباح</h2>
    <div class="publisher publisher--spine">
      <span class="publisher__mark"></span>
      <span class="publisher__name">دار النخيل</span>
    </div>
  </section>

  <section class="cover cover--front" role="img" aria-label="Soft pattern of leaves and branches over a magenta gradient">
    <svg class="heart-icon" viewBox="0 0 48 48" aria-hidden="true">
      <path d="M24 42 C10 32 4 24 4 16 C4 9 9 5 15 5 C19 5 22 7 24 11 C26 7 29 5 33 5 C39 5 44 9 44 16 C44 24 38 32 24 42 Z"
            fill="none" stroke="var(--ink)" stroke-width="2.2" stroke-linejoin="round"/>
    </svg>
    <h1 class="book-title">الواحة - نغمة صباح</h1>
    <p class="year">1440- 2018</p>
    <div class="publisher publisher--front">
      <span class="publisher__mark"></span>
      <span class="publisher__name">دار النخيل</span>
    </div>
  </section>
</div>
</body>
</html>
```